Flyer Design

I'm looking for a new flyer design to help promote our landscape company, and some of our main service for the up and coming season. We're trying to position ourselves as a leader in our market, so obviously quality is important to us.

Our current promotion is 25% off the first month with signup of annual service.

Phone Number: (816) 555-0193
Website: gardelvista.com
Our tagline: "Your hands are full... Let us help"

The call to action: direct them to our website for a detailed list of services and to receive a free quote.

You're welcome to add your own wording and punctuation. If I like the design I will provide feedback accordingly.

I have attached a jpg of our logo to help with design colors. I will provide the vector file upon completion of this project.

Also, I've attached a few photos that I had on hand of our companies work that may help with the design. Obviously I don't want to use them all, but there are a couple just to help out. I'm not opposed to stock photos either.
Thanks

Target Market(s)

We market to high end customers, generally with home between $500k-$2mil, or household income over $200k. Quality and creativity are most important to us.

Industry/Entity Type

Landscape

Requirements
Must have
• Creativity, easy to read, modern style.

```html
<!DOCTYPE html>
<html lang="en">
<head>
<meta charset="utf-8">
<title>Gardel Vista – Lawn Service Flyer</title>
<link rel="stylesheet" href="https://fonts.googleapis.com/css2?family=Barlow:wght@600;700&family=Graduate&family=Libre+Baskerville:wght@400;700&display=swap">
<style>
  :root {
    --ink: #0b0b0b;
    --gold: #f8c61c;
    --mint: #d8f2c2;
    --offer: rgba(214, 245, 176, 0.62);
    --white: #ffffff;
    --cream: #f6eab0;
    --brand-red: #e2352b;
  }
  html, body { margin: 0; padding: 0; overflow: hidden; background: #fff; }
  .flyer {
    position: relative;
    width: 925px;
    height: 1200px;
    overflow: hidden;
    background: var(--ink);
    font-family: "Barlow", Arial, sans-serif;
  }
  .backdrop { position: absolute; inset: 0; }
  .offer-headline {
    position: absolute; left: 64px; top: 42px; margin: 0;
    font: 700 150px/140px "Barlow", Arial, sans-serif;
    color: var(--offer); letter-spacing: 2px;
  }
  .offer-terms {
    position: absolute; left: 420px; top: 46px; margin: 0; width: 104px;
    font: 600 27px/38.5px "Barlow", Arial, sans-serif;
    color: var(--mint);
  }
  .brand {
    position: absolute; left: 620px; top: 88px;
    display: flex; align-items: center; gap: 12px;
  }
  .brand-dot { width: 34px; height: 34px; border-radius: 50%; background: var(--brand-red); }
  .brand-name {
    font: 36px/1 "Graduate", Georgia, serif; color: var(--white); letter-spacing: 1px;
  }
  .tagline {
    position: absolute; left: 563px; top: 266px; margin: 0;
    font: 80px/97px "Graduate", Georgia, serif;
    color: var(--white); letter-spacing: 2px;
  }
  .quote-cta {
    position: absolute; left: 69px; top: 428px; margin: 0;
    font: 31px/40px "Graduate", Georgia, serif;
    color: var(--gold); letter-spacing: 2px;
  }
  .services-title {
    position: absolute; left: 66px; top: 608px; margin: 0;
    font: 400 42px/1 "Libre Baskerville", Georgia, serif; color: var(--white);
  }
  .services-list {
    position: absolute; left: 66px; top: 696px; margin: 0; padding: 0; list-style: none;
  }
  .services-list li {
    position: relative; padding-left: 32px; height: 38px;
    font: 700 24px/38px "Libre Baskerville", Georgia, serif;
    color: var(--mint); letter-spacing: 0.5px;
  }
  .services-list li::before {
    content: ""; position: absolute; left: 2px; top: 13px;
    width: 11px; height: 11px; background: var(--gold);
  }
  .contact {
    position: absolute; left: 628px; top: 1058px; margin: 0;
    font: 700 22px/36px Arial, Helvetica, sans-serif; color: var(--cream);
  }
  .contact-line { display: flex; align-items: center; gap: 10px; }
</style>
</head>
<body>
<main class="flyer">
  <svg class="backdrop" width="925" height="1200" viewBox="0 0 925 1200">
    <defs>
      <linearGradient id="lawn-top" x1="0" y1="0" x2="0" y2="1">
        <stop offset="0" stop-color="#2f7c12"/>
        <stop offset="0.5" stop-color="#5cae22"/>
        <stop offset="1" stop-color="#3b8a17"/>
      </linearGradient>
      <linearGradient id="lawn-bottom" x1="0" y1="0" x2="1" y2="1">
        <stop offset="0" stop-color="#6fc52a"/>
        <stop offset="1" stop-color="#3d9418"/>
      </linearGradient>
      <linearGradient id="pattern-tone" x1="0" y1="0" x2="0" y2="1">
        <stop offset="0" stop-color="#f8c61c" stop-opacity="0.18"/>
        <stop offset="1" stop-color="#f8c61c" stop-opacity="0.55"/>
      </linearGradient>
    </defs>
    <rect class="lawn-photo" role="img" aria-label="Close-up photo of a hand brushing across fresh green lawn grass" x="0" y="0" width="925" height="470" fill="url(#lawn-top)"/>
    <rect class="lawn-photo" role="img" aria-label="Photo of lush green lawn grass" x="0" y="900" width="925" height="300" fill="url(#lawn-bottom)"/>
    <path class="dark-band" d="M0 458 H925 V1010 C800 995 640 1005 520 1040 C360 1085 170 1010 0 965 Z" fill="var(--ink)"/>

    <rect class="growth-pattern" role="img" aria-label="Decorative pattern of yellow dots on stems along a curving line" x="0" y="925" width="925" height="125" fill="url(#pattern-tone)"/>

    <g class="cta-frame" fill="none" stroke="var(--gold)" stroke-width="5" stroke-dasharray="20 11">
      <path d="M327 506 H543 V242 H876 V880 H473"/>
      <path d="M473 880 L430 925 L585 1118"/>
    </g>
    <path class="cta-arrow" d="M578 1106 L598 1118 L578 1130 Z" fill="var(--gold)"/>
    <path class="quote-mark" d="M210 474 H280 V532 L262 554 H220 L240 532 H210 Z" fill="var(--gold)"/>
  </svg>

  <h1 class="offer-headline">25%<br>OFF</h1>
  <p class="offer-terms">For the first month, When you sign up for weekly lawn</p>

  <div class="brand">
    <span class="brand-dot"></span>
    <span class="brand-name">GARDEL VISTA</span>
  </div>

  <h2 class="tagline">YOUR<br>HANDS<br>ARE<br>FULL...<br>LET US<br>HELP</h2>

  <p class="quote-cta">TO RECEIVE<br>A FREE<br>QUOTE</p>

  <h3 class="services-title">OUR SERVICES</h3>
  <ul class="services-list">
    <li>MOWING</li>
    <li>BRUSH &amp; TREE TRIMMING</li>
    <li>INSECT MANAGEMENT</li>
    <li>SNOW REMOVAL</li>
    <li>ICE TREATMENT</li>
    <li>AREATION SERVICES</li>
  </ul>

  <div class="contact">
    <div class="contact-line">
      <svg width="18" height="26" viewBox="0 0 18 26" aria-hidden="true">
        <rect x="2" y="2" width="14" height="22" rx="2" fill="none" stroke="var(--cream)" stroke-width="2"/>
        <rect x="5" y="5" width="8" height="9" fill="var(--cream)"/>
        <circle cx="9" cy="19" r="1.8" fill="var(--cream)"/>
      </svg>
      <span>(816) 555-0193</span>
    </div>
    <div class="contact-line">
      <svg width="24" height="20" viewBox="0 0 24 20" aria-hidden="true">
        <rect x="1" y="1" width="22" height="14" rx="1" fill="none" stroke="var(--cream)" stroke-width="2"/>
        <circle cx="7" cy="8" r="3" fill="var(--cream)"/>
        <rect x="12" y="5" width="8" height="2" fill="var(--cream)"/>
        <rect x="12" y="9" width="8" height="2" fill="var(--cream)"/>
        <rect x="8" y="16" width="8" height="3" fill="var(--cream)"/>
      </svg>
      <span>gardelvista.com</span>
    </div>
  </div>
</main>
</body>
</html>
```